Make a medical leaflet for my patients undergoing ankle blocks

I have a very boring text only leaflet I would like to turn into a professional appealing medical leaflet to give to my patients. I would like to get this onto two pages of a4 if possible and its intended for electronic distribution mainly.
This will be for patients so it must be professional.
It must also contain a copyright logo on it and my name near the start (Dr Tobias Renner) so my colleagues can't use it easily.
Target Market(s)
Patients undergoing surgery
Industry/Entity Type
Medical
Other font styles liked:
- no idea, you tell me
Requirements
Must have
- the information contained on the attachment
- look professional
- a copyright on it
Nice to have
- the fernbrook clinic logo
Should not have
- Any spelling, grammatical or linguistic errors
- Any font less than size 12

```html
<!DOCTYPE html>
<html lang="en">
<head>
<meta charset="utf-8">
<title>Ankle Block – Patient Information</title>
<link rel="stylesheet" href="https://fonts.googleapis.com/css2?family=EB+Garamond:ital,wght@0,400;1,400&family=Teko:wght@400;500&display=swap">
<style>
  :root {
    --blue: #1a95d3;
    --blue-deep: #1d63a0;
    --blue-bright: #10aee8;
    --blue-pale: #a9d9f2;
    --blue-mist: #d3ecf9;
    --text: #3c3c3c;
    --white: #ffffff;
  }
  * { margin: 0; padding: 0; box-sizing: border-box; }
  html, body { width: 878px; height: 1200px; overflow: hidden; background: var(--white); }
  .leaflet {
    position: relative; width: 878px; height: 1200px;
    font-family: "EB Garamond", Garamond, serif; color: var(--text);
    font-size: 13.6px; line-height: 18.2px;
  }
  .masthead { position: absolute; left: 0; top: 0; width: 878px; height: 320px; }
  .masthead svg { display: block; }
  .benefits {
    position: absolute; right: 38px; top: 30px; text-align: right;
    font-family: "Teko", sans-serif; color: var(--blue-mist);
    font-weight: 400; letter-spacing: 0.5px; line-height: 30px;
  }
  .benefits h2 { font-weight: 400; font-size: 33px; margin-bottom: 14px; }
  .benefits li { list-style: none; font-size: 29px; }
  .content { position: absolute; left: 0; top: 298px; width: 878px; padding-right: 34px; }
  .section-title {
    position: relative; font-family: "Teko", sans-serif; font-weight: 500;
    color: var(--blue); font-size: 33px; line-height: 32px; padding-left: 57px;
    letter-spacing: 0.3px;
  }
  .section-title::before {
    content: ""; position: absolute; left: 0; top: -2px; width: 30px; height: 29px;
    background: var(--blue-deep);
  }
  .lede, .sub {
    font-style: italic; color: var(--blue); font-size: 15px;
  }
  .lede { padding-left: 57px; margin-bottom: 2px; }
  .risks { list-style: none; padding-left: 82px; }
  .risks li { position: relative; margin-bottom: 2px; }
  .risks li::before {
    content: ""; position: absolute; left: -20px; top: 5px;
    border-left: 6px solid var(--blue); border-top: 4.5px solid transparent; border-bottom: 4.5px solid transparent;
  }
  .options { display: flex; gap: 12px; color: var(--blue); padding-left: 2px; }
  .options span::before {
    content: ""; display: inline-block; margin-right: 8px; vertical-align: 2px;
    border-bottom: 6px solid var(--text); border-left: 4.5px solid transparent; border-right: 4.5px solid transparent;
  }
  .indent-1 { padding-left: 57px; }
  .indent-2 { padding-left: 52px; }
  .howto { margin-top: 16px; }
  .sub { padding-left: 50px; margin-top: 4px; }
  .how p { padding-left: 50px; text-align: justify; }
  .how p.gap { margin-top: 9px; }
  .how p.tight { margin-top: 3px; }
  .footer-band { position: absolute; left: 0; bottom: 0; width: 878px; height: 20px; background: var(--blue); }
</style>
</head>
<body>
<div class="leaflet">
  <header class="masthead">
    <svg width="878" height="320" viewBox="0 0 878 320" aria-hidden="false">
      <rect x="0" y="0" width="878" height="280" fill="var(--blue)"/>
      <path d="M0,0 L0,240 C40,100 260,20 640,0 Z" fill="var(--white)"/>
      <rect role="img" aria-label="Illustration of runners in motion with flowing light lines" x="110" y="40" width="560" height="240" rx="120" fill="#4fb4e4" opacity="0.35"/>
      <g class="shapes-left">
        <path d="M7,240 A40,40 0 0 1 47,200 L47,240 Z" fill="var(--blue-deep)"/>
        <path d="M47,200 A40,40 0 0 1 87,240 L47,240 Z" fill="var(--blue-bright)"/>
        <path d="M7,280 A40,40 0 0 1 47,240 L47,280 Z" fill="var(--blue-pale)"/>
        <path d="M47,240 L87,240 A40,40 0 0 1 47,280 Z" fill="var(--blue-deep)"/>
        <path d="M87,280 A40,40 0 0 1 127,240 L127,280 Z" fill="var(--blue-pale)"/>
        <path d="M127,240 A40,40 0 0 1 167,280 L127,280 Z" fill="var(--blue-mist)"/>
      </g>
      <g class="shapes-right">
        <path d="M683,280 L738,280 L738,315 A55,35 0 0 1 683,280 Z" fill="var(--blue-pale)"/>
        <path d="M738,280 L738,350 A35,70 0 0 0 773,280 Z" fill="var(--blue-bright)"/>
        <path d="M788,280 L818,280 L818,314 A30,34 0 0 1 788,280 Z" fill="#86c7ea"/>
        <path d="M818,280 L848,280 A30,34 0 0 1 818,314 Z" fill="var(--blue-mist)"/>
      </g>
    </svg>
    <div class="benefits">
      <h2>WHAT ARE THE BENEFITS</h2>
      <ul>
        <li>FASTER RECOVERY</li>
        <li>PAIN RELIEF</li>
        <li>LESS NAUSEA &amp; VOMITING</li>
      </ul>
    </div>
  </header>

  <main class="content">
    <section class="risks-section">
      <h2 class="section-title">WHAT ARE THE RISKS?</h2>
      <p class="lede">As with all injections, there is the risk of bruising, bleeding and infection.</p>
      <ul class="risks">
        <li>Nerve Damage - Occurs 1 in 5000 nerve blocks. Creates an area of numbness or weakness paralysis in some / all the foot. Majority of nerve injuries will heal themselves within a year. There is no treatment to fix it. If the block has not worn off after 72 hours please let me know.</li>
        <li>Failure - The success rate with ankle blocks is 98 - 99%. Some blocks will fail, partially or totally. If total failure, I will discuss repeating the block with your consent.</li>
        <li>Pain during operation - If you choose to have wide awake surgery or surgery under sedation<br>The surgery will stop and I will discuss three options with you
          <div class="options"><span>more numbing liquid to be injected by the surgeon</span><span>more sedation / painkiller</span><span>having a general anaesthetic</span></div>
        </li>
      </ul>
      <p class="indent-1">If you decide to undergo surgery awake or sedated, there is a risk you will need to have a general anaesthetic if you feel pain. This is why the starvation instructions of awake surgery and general anaesthesia are the same.</p>
    </section>

    <section class="how howto">
      <h2 class="section-title">HOW IS IT DONE</h2>
      <p class="sub">If you choose awake surgery or surgery with sedation -</p>
      <p>Numbing liquid is injected around the nerves which supply your foot. The ankle block takes 5 - 10 minutes to perform and requires 4 - 5 injections. Approximately 10 - 20 minutes to make your foot numb to pain. I will check the ankle block is working before we start surgery using cold spray. Sensations of touch, pressure, vibration and movement will still be felt. I will use a screen so you can’t see the surgery (unless you would like to see). Some patients bring headphones to block out the noise of the operation.</p>
      <p class="sub">If you choose a General anaesthetic -</p>
      <p>I will perform the ankle block after I start the general anaesthetic. You should wake up from your surgery with a comfortable and numb foot/feet. If you wake in pain, we can repeat the ankle block or provide traditional painkillers.</p>
      <p class="tight">Whatever you choose, there will be a cannula placed in your hand and heart and oxygen monitoring throughout.</p>
      <p class="sub">After surgery</p>
      <p>You will go to the recovery area and then onto the ward when you are ready. It will be difficult to walk while the block is working so physiotherapists will help you first walk. If you need crutches they will teach you how to use them.</p>
      <p class="gap">Your foot will be numb and so you will not feel where your foot is in relation to nearby objects. As a result, it is easy to knock your foot. Please take extra care while your foot is still numb.</p>
      <p class="gap">As the block wears off, the foot may feel slightly painful, tingly or hot. At this point you should take your painkillers I have prescribed. Depending on your medical history you will have up to three painkillers. I would suggest to start with all three. You will also have an anti - sickness prescribed if one of the painkillers (typically codeine or morphine) makes you feel sick.</p>
      <p class="gap">Occasionally (1 - 2%), pain when the block wears off will be severe. In this case contact your surgeon’s secretary. We can use stronger pain medication, but there will be a charge in writing and getting the private prescription to you (please see my terms of business) via courier.</p>
      <p class="sub">The alternative</p>
      <p>If you do not have an ankle block your surgery can still proceed. Post operative pain can be managed with traditional painkillers. However, you are more likely to need an overnight stay or feel sick after the anaesthetic.</p>
      <p class="tight">If you have any further questions about an ankle block I will see you the day of your surgery. Alternatively, you can request the following optional services (as mentioned in my terms of business).</p>
    </section>
  </main>

  <div class="footer-band"></div>
</div>
</body>
</html>
```